Cleaning services Business Card Design

I need a business card design for my Cleaning business. I would like perhaps emphasis on the company name, Muddle to Marvel. Maybe the Muddle would to dirty and the marvel would have sprinkles.

Industry/Entity Type

Business

Contact Information for Business Card

Muddle to Marvel Cleaning Services, Tomas Ordell, Industrial, Commercial, & Residential 415-806-2147

```html
<!DOCTYPE html>
<html lang="en">
<head>
<meta charset="utf-8">
<title>Muddle to Marvel Cleaning Services – Business Card</title>
<link rel="stylesheet" href="https://fonts.googleapis.com/css2?family=Open+Sans:wght@400;600&display=swap">
<style>
  :root {
    --page-bg: #2b2b2b;
    --card-bg: #121212;
    --card-edge: #1d1d1d;
    --brand-green: #8cc63f;
    --brand-blue: #2f5ff2;
    --divider: rgba(255, 255, 255, 0.06);
  }
  * { box-sizing: border-box; margin: 0; padding: 0; }
  html, body {
    width: 1200px;
    height: 900px;
    overflow: hidden;
    background: var(--page-bg);
    font-family: "Open Sans", Arial, sans-serif;
  }
  .card-set {
    position: absolute;
    top: 300px;
    left: 60px;
    display: flex;
    gap: 40px;
  }
  .card {
    position: relative;
    width: 520px;
    height: 300px;
    border-radius: 22px;
    background: var(--card-bg);
    border: 1px solid var(--card-edge);
    overflow: hidden;
  }

  /* Front */
  .card-front .brand-mark {
    position: absolute;
    left: 40px;
    top: 92px;
    display: flex;
    align-items: center;
    gap: 12px;
  }
  .brand-square {
    width: 26px;
    height: 26px;
    border: 3px solid var(--brand-green);
  }
  .brand-name {
    color: var(--brand-green);
    font-weight: 600;
    font-size: 22px;
    letter-spacing: 0.2px;
  }
  .card-front .divider {
    position: absolute;
    left: 290px;
    top: 0;
    width: 1px;
    height: 210px;
    background: var(--divider);
  }
  .contact {
    position: absolute;
    left: 318px;
    top: 60px;
  }
  .contact-name {
    color: var(--brand-green);
    font-weight: 600;
    font-size: 15px;
  }
  .contact-phone {
    margin-top: 8px;
    display: flex;
    align-items: center;
    gap: 6px;
    color: var(--brand-blue);
    font-size: 12px;
  }
  .contact-phone svg { width: 10px; height: 10px; fill: var(--brand-green); }
  .services {
    position: absolute;
    left: 40px;
    bottom: 42px;
    color: var(--brand-green);
    font-weight: 600;
    font-size: 15px;
    letter-spacing: 0.3px;
  }

  /* Back */
  .card-back {
    display: flex;
    flex-direction: column;
    align-items: center;
    justify-content: center;
  }
  .card-back .brand-square {
    width: 54px;
    height: 54px;
    border: 5px solid var(--brand-green);
    margin-bottom: 26px;
  }
  .company-name {
    color: var(--brand-blue);
    font-size: 19px;
    letter-spacing: 0.3px;
    text-transform: uppercase;
  }
  .company-type {
    margin-top: 2px;
    color: var(--brand-green);
    font-size: 17px;
    letter-spacing: 1.5px;
  }
</style>
</head>
<body>
  <main class="card-set">
    <section class="card card-front">
      <div class="brand-mark">
        <span class="brand-square"></span>
        <span class="brand-name">Muddle to Marvel</span>
      </div>
      <div class="divider"></div>
      <div class="contact">
        <p class="contact-name">Tomas Ordell</p>
        <p class="contact-phone">
          <svg viewBox="0 0 24 24" aria-hidden="true"><path d="M6.6 10.8a15.1 15.1 0 0 0 6.6 6.6l2.2-2.2a1 1 0 0 1 1-.25 11.4 11.4 0 0 0 3.6.57 1 1 0 0 1 1 1V20a1 1 0 0 1-1 1A17 17 0 0 1 3 4a1 1 0 0 1 1-1h3.5a1 1 0 0 1 1 1c0 1.25.2 2.45.57 3.57a1 1 0 0 1-.25 1z"/></svg>
          415-806-2147
        </p>
      </div>
      <p class="services">INDUSTRIAL, COMMERCIAL &amp; RESIDENTIAL</p>
    </section>

    <section class="card card-back">
      <span class="brand-square"></span>
      <p class="company-name">Muddle to Marvel</p>
      <p class="company-type">Cleaning Services</p>
    </section>
  </main>
</body>
</html>
```